Wolkenfeld - a property developer - Website design

Hi all!
Exciting new project for you! :)
We are looking for some creative/modern designs to best represent us as a company.
Please have a look at the following link: huhu.wolkenfeld.eu to get an idea about who we are and what we do.
The 'Main Page' of the HP should be neatly arranged, easy to navigate, contain several pictures (changing every 10 seconds or so) that should reflect that we are property developers.
The navigation points ('About us', 'Projects' 'Investment', 'Contact Us', 'Legal Notice') should be included in the Design (again under every navigation point, pictures may be added - that reflect our profession and/or the subsection)
What we will need at the end of the day is a fully functional site - i.e: a site that is designed and programmed with backend/wordpress, to allow us to make changes anytime we feel like it.
Further questions?! Don't hesitate to contact me! Thanks :)
Target Market(s)
Real Estate Development/Building sector
Industry/Entity Type
Real Estate Development
Number of Pages Required
5+ page
Look and feel

```html
<!DOCTYPE html>
<html lang="en">
<head>
<meta charset="utf-8">
<title>Wolkenfeld – Property Development</title>
<link rel="stylesheet" href="https://fonts.googleapis.com/css2?family=Roboto:wght@300;400;700&family=Roboto+Condensed:wght@300;400;700&display=swap">
<style>
:root{
  --yellow:#ffd500;
  --dark:#2a2a2a;
  --darker:#151515;
  --black:#000;
  --white:#fff;
  --grey:#6b6b6b;
  --light:#e6e6e6;
}
*{box-sizing:border-box;margin:0;padding:0}
html,body{width:726px;height:1200px;overflow:hidden;background:var(--white)}
body{position:relative;font-family:'Roboto',sans-serif;color:var(--grey)}
.abs{position:absolute}

/* hero */
.hero{left:0;top:0;width:726px;height:400px;background:linear-gradient(120deg,#cfc3b0 0%,#e8dfd2 40%,#b9a58d 70%,#8e7a66 100%)}
.brand{left:28px;top:20px;display:flex;align-items:center;gap:8px}
.brand-square{width:22px;height:22px;background:var(--white)}
.brand-name{font-family:'Roboto Condensed',sans-serif;font-weight:700;font-size:28px;color:var(--white);letter-spacing:1px}
.menu-btn{right:28px;top:16px;width:40px;height:40px;background:var(--black);display:flex;flex-direction:column;justify-content:center;align-items:center;gap:5px}
.menu-btn span{display:block;width:18px;height:2px;background:var(--white)}
.hero-band{left:0;top:355px;width:726px;height:45px;background:rgba(255,255,255,.35)}
.dots{left:336px;top:366px;display:flex;gap:8px}
.dots span{width:11px;height:11px;border-radius:50%;background:var(--darker)}
.dots span.on{background:var(--white);border:2px solid var(--darker)}

/* gallery */
.gallery{left:0;top:400px;width:726px;height:156px;display:flex}
.tile{flex:1;height:100%}
.tile.t1{background:linear-gradient(#6c7480,#3d4148)}
.tile.t2{background:linear-gradient(#9aa3ab,#5b5f63)}
.tile.t3{background:linear-gradient(#a9b2bb,#6e6a64)}
.tile.t4{background:linear-gradient(#8c8f93,#4d4f52)}
.view-all{left:10px;top:405px;width:160px;height:146px;background:rgba(40,40,40,.8);border:1px solid rgba(255,255,255,.3);display:flex;flex-direction:column;align-items:center;justify-content:center;gap:8px}
.view-all span{font-size:13px;color:var(--yellow)}

/* who we are */
.who-bg{left:0;top:556px;width:726px;height:150px}
.who-title{left:80px;top:588px;font-family:'Roboto Condensed',sans-serif;font-weight:300;font-size:27px;color:var(--darker);letter-spacing:1px}
.who-sub{left:92px;top:622px;font-size:10px;color:#5a4a00}
.btn{display:inline-flex;align-items:center;justify-content:center;border-radius:20px;font-size:11px}
.btn-dark{background:var(--black);color:var(--white)}
.btn-light{background:var(--white);color:var(--darker);border:1px solid #888}
.who-btn{left:92px;top:643px;width:84px;height:27px}
.who-text{left:388px;top:604px;width:310px;font-size:10.5px;line-height:15px;color:#ddd}

/* investments / legal */
.col-title{font-family:'Roboto Condensed',sans-serif;font-weight:300;font-size:27px;color:var(--darker);letter-spacing:.5px}
.inv-title{left:72px;top:735px}
.legal-title{left:440px;top:735px}
.rule{height:1px;background:var(--light)}
.inv-rule{left:40px;top:775px;width:300px}
.legal-rule{left:392px;top:775px;width:300px}
.inv-text{left:76px;top:787px;width:250px;font-size:8.5px;line-height:12.5px}
.legal-list{left:392px;top:786px;width:300px;display:flex;gap:30px;font-size:8.5px;line-height:12.5px}
.inv-btn{left:143px;top:872px;width:84px;height:27px}
.legal-btn{left:520px;top:872px;width:84px;height:27px}

/* contact */
.contact-bg{left:0;top:920px;width:726px;height:163px}
.form{left:70px;top:934px;width:330px}
.field-row{display:flex;gap:10px;margin-bottom:8px}
.field{flex:1;height:20px;background:rgba(255,255,255,.08);border:1px solid rgba(255,255,255,.15);font-size:9px;color:#ccc;padding:4px 6px}
.field.msg{height:48px}
.submit{left:188px;top:1052px;width:84px;height:24px}
.touch-title{left:498px;top:960px;font-family:'Roboto Condensed',sans-serif;font-weight:400;font-size:15px;color:var(--darker)}
.touch-list{left:498px;top:986px;font-size:9px;line-height:12px;color:var(--darker)}
.touch-item{display:flex;gap:8px;margin-bottom:8px;align-items:flex-start}

/* footer */
.footer{left:0;top:1083px;width:726px;height:117px;background:var(--darker)}
.nav{left:0;top:1124px;width:726px;display:flex;justify-content:center;gap:26px;font-size:9.5px;color:#bbb}
.nav .active{color:var(--yellow)}
.foot-rule{left:30px;top:1150px;width:666px;height:1px;background:#333}
.copy{left:30px;top:1172px;font-size:9.5px;color:#bbb}
.copy b{color:var(--yellow);font-weight:400}
.social{right:40px;top:1165px;display:flex;gap:8px}
.social span{width:24px;height:24px;border-radius:50%;background:var(--yellow)}
</style>
</head>
<body>

<div class="abs hero" role="img" aria-label="Photo of a smiling couple receiving house keys and documents from an estate agent"></div>
<div class="abs brand"><span class="brand-square"></span><span class="brand-name">WOLKENFELD</span></div>
<div class="abs menu-btn"><span></span><span></span><span></span></div>
<div class="abs hero-band"></div>
<div class="abs dots"><span></span><span class="on"></span><span></span></div>

<div class="abs gallery">
  <div class="tile t1" role="img" aria-label="Photo of a modern residential project at dusk"></div>
  <div class="tile t2" role="img" aria-label="Photo of a contemporary villa with pool"></div>
  <div class="tile t3" role="img" aria-label="Photo of a new family house exterior"></div>
  <div class="tile t4" role="img" aria-label="Photo of a roof extension project"></div>
</div>
<div class="abs view-all">
  <svg width="20" height="20" viewBox="0 0 20 20"><circle cx="8" cy="8" r="6" fill="none" stroke="#fff" stroke-width="2.2"/><line x1="12.5" y1="12.5" x2="18" y2="18" stroke="#fff" stroke-width="2.5"/></svg>
  <span>View All Projects</span>
</div>

<svg class="abs who-bg" width="726" height="150" viewBox="0 0 726 150">
  <polygon points="0,0 310,0 330,140 0,140" fill="#ffd500"/>
  <polygon points="310,0 726,0 726,150 330,150" fill="#2a2a2a"/>
  <polygon points="0,140 330,140 332,150 0,150" fill="#fff"/>
</svg>
<div class="abs who-title">WHO WE ARE</div>
<div class="abs who-sub">Know About Wolkenfeld</div>
<div class="abs btn btn-dark who-btn">Read More</div>
<p class="abs who-text">Wolkenfeld is a combination of potent companies pursuing a common goal: the realisation of modern, sustainable housing projects for highest demands in Vienna. Our building companies' efforts are concentrating on the two core areas of new developments and roof extensions.</p>

<div class="abs col-title inv-title">OUR INVESTMENTS</div>
<div class="abs col-title legal-title">OUR LEGAL NOTICE</div>
<div class="abs rule inv-rule"></div>
<div class="abs rule legal-rule"></div>
<p class="abs inv-text">Invest now in the future of housing. Starting with an investment from 300.000 Euro you can participate in an exclusive roof extension or new development project by Wolkenfeld. Benefit from uniquely successful projects with high values and an entry to the land register.</p>
<div class="abs legal-list">
  <div>WOLKENFELD 01 GmbH<br>WOLKENFELD 02 GmbH</div>
  <div>Lindenweg 4/TOP 7<br>1010 Vienna – Austria<br>Phone +43 1 555 0142<br>Fax +43 1 555 0143<br>e-mail info@wolkenfeld.eu</div>
</div>
<div class="abs btn btn-light inv-btn">Get More</div>
<div class="abs btn btn-dark legal-btn">Get More</div>

<svg class="abs contact-bg" width="726" height="163" viewBox="0 0 726 163">
  <rect width="726" height="163" fill="#2a2a2a"/>
  <polygon points="430,10 726,10 726,163 458,163" fill="#ffd500"/>
</svg>
<div class="abs form">
  <div class="field-row"><div class="field">Name</div><div class="field">Email Id</div></div>
  <div class="field-row"><div class="field msg">Message</div></div>
</div>
<div class="abs btn btn-light submit">Submit</div>
<div class="abs touch-title">KEEP IN TOUCH WITH US</div>
<div class="abs touch-list">
  <div class="touch-item">
    <svg width="10" height="12" viewBox="0 0 10 12"><path d="M5 0a4 4 0 0 1 4 4c0 3-4 8-4 8S1 7 1 4a4 4 0 0 1 4-4z" fill="#151515"/><circle cx="5" cy="4" r="1.5" fill="#ffd500"/></svg>
    <span>Lindenweg 4/TOP 7<br>1010 Vienna – Austria</span>
  </div>
  <div class="touch-item">
    <svg width="10" height="12" viewBox="0 0 10 12"><path d="M2 0h2l1 3-1.5 1a6 6 0 0 0 3 3.5L8 6l2 1v2c0 1-1 2-2 2C4 10 0 6 0 2 0 1 1 0 2 0z" fill="#151515"/></svg>
    <span>+43 1 555 0142</span>
  </div>
  <div class="touch-item">
    <svg width="12" height="10" viewBox="0 0 12 10"><rect x="0" y="1" width="12" height="8" fill="#151515"/><path d="M0 1l6 4 6-4" fill="none" stroke="#ffd500" stroke-width="1"/></svg>
    <span>info@wolkenfeld.eu</span>
  </div>
</div>

<div class="abs footer"></div>
<nav class="abs nav"><span class="active">Home</span><span>About Us</span><span>Projects</span><span>Investments</span><span>Legal Notice</span><span>Contact Us</span></nav>
<div class="abs foot-rule"></div>
<div class="abs copy">© <b>Wolkenfeld</b> – 2016, All Rights Reserved.</div>
<div class="abs social"><span></span><span></span><span></span></div>

</body>
</html>
```